Tarvel Ridge LLC

Need Professional Business cards for New Investment Fund

Target Market(s)

High Quality investors

Industry/Entity Type

Financial

Contact Information for Business Card

Phone Number +1 555 284 6193
Name Pavel Orlinsky
Title Fund Manager
email po@FundTarvel.example
Website www.FundTarvel.example

Colors

Designer to choose colors to be used in the design.

Requirements
Must have
• Must have our Logo and all of the above. Must be made so lettering and loge can be raised

```html
<!DOCTYPE html>
<html lang="en">
<head>
<meta charset="utf-8">
<title>Tarvel Ridge LLC – Business Card</title>
<link rel="stylesheet" href="https://fonts.googleapis.com/css2?family=Mulish:wght@400;600;700&display=swap">
<style>
  :root {
    --page-bg: #ecebe8;
    --card-bg: #ffffff;
    --ink: #1f1f1f;
    --accent: #c8dc7c;
    --rule: #2a2a2a;
  }
  * { box-sizing: border-box; margin: 0; padding: 0; }
  html, body {
    width: 1200px;
    height: 1200px;
    overflow: hidden;
    background: var(--page-bg);
    font-family: "Mulish", sans-serif;
    color: var(--ink);
  }
  .canvas {
    position: relative;
    width: 1200px;
    height: 1200px;
  }
  .business-card {
    position: absolute;
    left: 100px;
    top: 315px;
    width: 1000px;
    height: 570px;
    background: var(--card-bg);
    box-shadow: 0 14px 40px rgba(0,0,0,0.12);
  }
  .brand {
    position: absolute;
    left: 0;
    top: 0;
    width: 430px;
    height: 100%;
    display: flex;
    align-items: center;
    justify-content: center;
    gap: 18px;
  }
  .brand-square {
    width: 34px;
    height: 34px;
    background: var(--accent);
  }
  .brand-name {
    font-weight: 700;
    font-size: 40px;
    letter-spacing: 1px;
    text-transform: uppercase;
    color: var(--ink);
  }
  .divider {
    position: absolute;
    left: 430px;
    top: 36px;
    width: 3px;
    height: 510px;
    background: var(--rule);
  }
  .identity {
    position: absolute;
    left: 500px;
    top: 190px;
    width: 440px;
    text-align: center;
  }
  .person-name {
    font-weight: 600;
    font-size: 44px;
    padding-bottom: 6px;
    border-bottom: 3px solid var(--rule);
  }
  .person-title {
    font-weight: 400;
    font-size: 32px;
    margin-top: 6px;
  }
  .contacts {
    position: absolute;
    left: 470px;
    top: 400px;
    list-style: none;
  }
  .contact {
    display: flex;
    align-items: center;
    gap: 20px;
    font-size: 26px;
    line-height: 45px;
  }
  .contact svg { width: 22px; height: 22px; flex: none; }
</style>
</head>
<body>
<main class="canvas">
  <article class="business-card">
    <div class="brand">
      <span class="brand-square"></span>
      <span class="brand-name">Tarvel Ridge</span>
    </div>
    <div class="divider"></div>
    <div class="identity">
      <h1 class="person-name">Pavel Orlinsky</h1>
      <p class="person-title">Fund Manager</p>
    </div>
    <ul class="contacts">
      <li class="contact">
        <svg viewBox="0 0 22 22" aria-hidden="true"><rect width="22" height="22" rx="2" fill="#1f1f1f"/><path d="M7 5c-1 1-1.5 2.5-1 4.5 1 3 3.5 6 6.5 7 1.5.5 3 .3 4-.8l-2.4-2.3-1.6 1c-1.7-.8-3.2-2.4-4-4.2l1-1.5L7 5z" fill="#fff"/></svg>
        <span>+1 555 284 6193</span>
      </li>
      <li class="contact">
        <svg viewBox="0 0 22 22" aria-hidden="true"><rect width="22" height="22" rx="2" fill="#1f1f1f"/><rect x="4" y="6" width="14" height="10" fill="none" stroke="#fff" stroke-width="1.6"/><path d="M4 6l7 6 7-6" fill="none" stroke="#fff" stroke-width="1.6"/></svg>
        <span>po@FundTarvel.example</span>
      </li>
      <li class="contact">
        <svg viewBox="0 0 22 22" aria-hidden="true"><rect width="22" height="22" rx="2" fill="#1f1f1f"/><circle cx="11" cy="11" r="6.5" fill="none" stroke="#fff" stroke-width="1.4"/><ellipse cx="11" cy="11" rx="3" ry="6.5" fill="none" stroke="#fff" stroke-width="1.2"/><path d="M4.5 11h13" stroke="#fff" stroke-width="1.2"/></svg>
        <span>www.FundTarvel.example</span>
      </li>
    </ul>
  </article>
</main>
</body>
</html>
```